Harmony Swift Care Business card

We want a business card that matches our business theme. Our website is www.swiftcarehub.example
The company name is Harmony Swift Care
The persons having the business cards will be doctors
My logo is attached.
We have a drive-thru medical center where our motto is Fast, Reliable, and Convenient. Our goal is to change the medical space while utilizing technologies, keeping a professional and clean look

Medical

Info on the card should be: Name, Position, Cell number, website, email address, possibly the office line as well

Requirements
Must have
• Logo
Nice to have
• Professional medical feel with our logo colors incorporated

```html
<!DOCTYPE html>
<html lang="en">
<head>
<meta charset="utf-8">
<title>Harmony Swift Care – Business Card</title>
<link href="https://fonts.googleapis.com/css2?family=Jost:wght@400;500;600;700&display=swap" rel="stylesheet">
<style>
  :root {
    --navy: #1e52a6;
    --sky: #3fc8f4;
    --paper: #ffffff;
    --stage: #eef1f5;
    --ink: #1c2a44;
  }
  * { margin: 0; padding: 0; box-sizing: border-box; }
  html, body { width: 1200px; height: 800px; overflow: hidden; }
  body {
    background: var(--stage);
    font-family: "Jost", Arial, sans-serif;
    position: relative;
  }
  .card {
    position: absolute;
    top: 245px;
    width: 540px;
    height: 309px;
    background: var(--paper);
    overflow: hidden;
    box-shadow: 0 10px 30px rgba(30, 60, 110, 0.15);
  }
  .card--front { left: 40px; }
  .card--back { left: 620px; }
  .card-bg { position: absolute; inset: 0; }

  .company-name {
    position: absolute;
    font-weight: 600;
    font-size: 21px;
    line-height: 1;
    color: var(--navy);
    white-space: nowrap;
  }
  .card--front .company-name { left: 36px; top: 142px; }
  .card--back .company-name { left: 36px; top: 46px; }

  .holder {
    position: absolute;
    left: 370px;
    top: 34px;
    font-weight: 500;
    line-height: 1.1;
  }
  .holder-name { font-size: 20px; color: var(--sky); }
  .holder-position { font-size: 20px; color: var(--paper); }

  .contacts {
    position: absolute;
    right: 22px;
    top: 128px;
    list-style: none;
    display: flex;
    flex-direction: column;
    gap: 9px;
  }
  .contact {
    display: flex;
    align-items: center;
    justify-content: flex-end;
    gap: 10px;
    color: var(--paper);
    font-size: 14px;
  }
  .contact-icon {
    width: 24px; height: 24px;
    border-radius: 50%;
    background: var(--sky);
    display: flex; align-items: center; justify-content: center;
  }
  .contact-icon svg { width: 14px; height: 14px; }

  .scene {
    position: absolute;
    right: 0; top: 40px;
    width: 300px; height: 269px;
    background: linear-gradient(160deg, #eef3fb 0%, #c9dcf3 45%, #6f9fe0 75%, #d9dee8 100%);
  }
</style>
</head>
<body>

  <section class="card card--front" aria-label="Business card front">
    <svg class="card-bg" viewBox="0 0 540 309" aria-hidden="true">
      <path d="M230 0 H540 V309 H0 V300 C140 300 290 250 292 170 C294 110 200 60 230 0 Z" fill="var(--sky)"/>
      <path d="M240 0 H540 V309 H10 V309 C150 305 298 255 300 170 C302 110 212 60 240 0 Z" fill="var(--paper)"/>
      <path d="M252 0 H540 V309 H40 C170 300 310 255 312 170 C314 110 224 60 252 0 Z" fill="var(--navy)"/>
    </svg>

    <p class="company-name">Harmony Swift Care</p>

    <div class="holder">
      <p class="holder-name">Name</p>
      <p class="holder-position">Position</p>
    </div>

    <ul class="contacts">
      <li class="contact">Cell number
        <span class="contact-icon">
          <svg viewBox="0 0 14 14" fill="none" stroke="#fff" stroke-width="1.4"><rect x="4" y="1" width="6" height="12" rx="1"/><line x1="6" y1="11" x2="8" y2="11"/></svg>
        </span>
      </li>
      <li class="contact">Office line
        <span class="contact-icon">
          <svg viewBox="0 0 14 14" fill="#fff"><path d="M3 1.5 L5 1.5 L6 4.5 L4.6 5.6 C5.4 7.3 6.7 8.6 8.4 9.4 L9.5 8 L12.5 9 L12.5 11 C12.5 12 11.5 12.6 10.5 12.4 C6 11.6 2.4 8 1.6 3.5 C1.4 2.5 2 1.5 3 1.5 Z"/></svg>
        </span>
      </li>
      <li class="contact">Website
        <span class="contact-icon">
          <svg viewBox="0 0 14 14" fill="none" stroke="#fff" stroke-width="1.1"><circle cx="7" cy="7" r="5.5"/><ellipse cx="7" cy="7" rx="2.4" ry="5.5"/><line x1="1.5" y1="7" x2="12.5" y2="7"/></svg>
        </span>
      </li>
      <li class="contact">Email address
        <span class="contact-icon">
          <svg viewBox="0 0 14 14" fill="none" stroke="#fff" stroke-width="1.2"><rect x="1.5" y="3" width="11" height="8"/><polyline points="1.5,3 7,8 12.5,3"/></svg>
        </span>
      </li>
    </ul>
  </section>

  <section class="card card--back" aria-label="Business card back">
    <p class="company-name">Harmony Swift Care</p>

    <div class="scene" role="img" aria-label="Illustration of a drive-thru clinic building with a doctor standing at the entrance and cars waiting alongside"></div>
  </section>

</body>
</html>
```